Flyer für Freizeiteinrichtung mit Teamkampf-Minispielen, Schwarzlicht-Minigolf und Pixel-Games
Zielgruppe
Wir sind eine Freizeiteinrichtung mit Teamkampf-Minispielen, Schwarzlicht-Minigolf und Pixel-Games
Aufgabenstellung
DINA5, 6 seitig, Wickelfalz. Text und Bilder werden komplett geliefert. Design an die Website angelehnt.

```html
<!DOCTYPE html>
<html lang="de">
<head>
<meta charset="utf-8">
<title>Zackfalke – Teambuilding Flyer Wickelfalz</title>
<link href="https://fonts.googleapis.com/css2?family=Orbitron:wght@400;500&family=Michroma&family=Inter:wght@400;500;600;700&display=swap" rel="stylesheet">
<style>
:root{
  --bg:#dcdcdc;
  --night:#0a1024;
  --purple:#1c1240;
  --pink:#e0348a;
  --cyan:#19b9ec;
  --cyan-bright:#2fd4ff;
  --text-light:#f2f4f8;
  --text-muted:#c9cfdb;
  --paper:#e4e4ea;
  --text-dark:#2b2f3a;
  --violet:#7a4bd8;
}
*{box-sizing:border-box;margin:0;padding:0}
html,body{width:1200px;height:2298px;overflow:hidden;background:var(--bg)}
body{font-family:"Inter",sans-serif;color:var(--text-light);position:relative}
.spread{position:absolute;left:50px;width:1100px;height:778px;overflow:hidden;box-shadow:0 10px 28px rgba(0,0,0,.28)}
.spread--outside{top:312px;background:var(--night)}
.spread--inside{top:1208px;background:linear-gradient(180deg,#0d0b22 0%,#1e1248 60%,#2a1460 100%)}
.panel{position:absolute;top:0;height:778px;width:367px;overflow:hidden}
.p1{left:0}.p2{left:367px}.p3{left:734px;width:366px}
.abs{position:absolute}
.heading{font-family:"Orbitron",sans-serif;font-weight:400;font-size:17px;line-height:1.18;letter-spacing:.3px;text-transform:uppercase;color:var(--pink)}
.body{font-size:11px;line-height:1.38;color:var(--text-muted)}
.body p+p{margin-top:8px}
.list{list-style:none;font-size:11px;line-height:1.35}
.list li{position:relative;padding-left:14px;margin-bottom:5px}
.list li::before{content:"›";position:absolute;left:0;top:-3px;font-size:16px;color:var(--pink);font-weight:700}
.photo{position:absolute}
/* outside */
.outside-p1{background:#050507}
.why{left:34px;top:40px;width:300px}
.why .list{margin-top:16px;color:var(--text-light)}
.why strong{display:block;font-size:11px;margin-top:2px}
.photo-toast{left:0;top:321px;width:367px;height:457px;background:radial-gradient(circle at 45% 40%,#d9b3c4 0,#8a5a7a 22%,#2a1930 55%,#08070c 100%)}
.photo-crowd{left:367px;top:150px;width:733px;height:430px;background:radial-gradient(ellipse at 60% 50%,#3a5f9c 0,#1c3a72 40%,#0b1737 80%)}
.band{left:367px;top:0;width:733px;height:778px}
.book{left:400px;top:40px;width:300px}
.book .body{margin-top:22px;color:var(--text-light)}
.contact{left:400px;top:540px;width:300px;font-size:11px;line-height:1.35;color:var(--text-light)}
.contact .entry{border-left:2px solid var(--cyan);padding-left:6px;margin-top:8px}
.contact .label{font-size:8.5px;font-weight:700;letter-spacing:1px;text-transform:uppercase}
.contact .value{font-size:12.5px}
.contact .loc{margin-top:10px;font-weight:600}
.contact .addr{margin-top:6px;font-size:10.5px}
.title{left:770px;top:38px;width:310px;font-family:"Michroma",sans-serif;font-size:23px;line-height:1.15;color:#fff}
.title-rule{left:770px;top:134px;width:86px;height:3px;background:#fff}
.sub{left:770px;top:150px;font-size:16px;letter-spacing:.3px;color:#fff}
.brand{left:918px;top:532px;font-family:"Michroma",sans-serif;font-size:17px;color:#fff;display:flex;align-items:center;gap:6px}
.brand .dot{width:9px;height:9px;border-radius:50%;background:var(--cyan)}
.ideal{left:770px;top:620px;width:300px;color:var(--text-light)}
.ideal .cap{font-size:12px;font-weight:500}
.ideal ul{list-style:none;margin-top:8px;border-left:2px solid var(--cyan);padding-left:12px;font-size:13px;line-height:1.6}
.bar{left:367px;top:739px;width:733px;height:39px;background:var(--cyan);display:flex;align-items:center;font-size:11px;font-weight:600;color:#0a1a30}
.bar span{position:absolute}
/* inside */
.team{left:34px;top:30px;width:310px}
.team .body{margin-top:18px;padding-left:12px;color:var(--text-light)}
.world{left:32px;top:310px;width:300px}
.card{position:absolute;border:2px solid var(--cyan-bright);border-radius:12px;background:rgba(12,10,30,.88);overflow:hidden;box-shadow:0 0 12px rgba(47,212,255,.45)}
.card-head{display:flex;align-items:center;gap:22px;padding:12px 10px 6px}
.card-tag{font-family:"Orbitron",sans-serif;font-size:11px;font-weight:500;color:var(--pink);letter-spacing:.5px;border:1px solid var(--pink);padding:3px 6px;border-radius:3px}
.card-title{font-size:12.5px;font-weight:700;color:#fff;line-height:1.2}
.card .body{padding:4px 10px;color:var(--text-light);font-size:10.8px}
.card .sub-cap{font-weight:700;color:#fff;font-size:11px;margin-top:4px}
.card .list{padding:4px 10px 0;color:var(--text-light);font-size:10.8px}
.card .list li{margin-bottom:3px}
.card-blacklight{left:22px;top:363px;width:321px;height:396px}
.card-team{left:390px;top:26px;width:322px;height:363px}
.card-pixel{left:390px;top:409px;width:322px;height:350px}
.ph-golf{left:0;bottom:0;width:100%;height:112px;border-top:2px solid var(--cyan-bright);background:linear-gradient(120deg,#5b2d9c,#d84aa0 35%,#3a7be0 65%,#6a2cb0)}
.ph-team{left:0;bottom:0;width:100%;height:167px;background:linear-gradient(160deg,#b9b3ad,#6b6964 50%,#2f3b2e)}
.ph-pixel{left:0;bottom:0;width:100%;height:180px;background:radial-gradient(ellipse at 50% 45%,#3fe05a 0,#148a2a 40%,#05200a 85%)}
.inside-p3{background:linear-gradient(160deg,#ecebf0,var(--paper) 60%,#d6d6de)}
.packages{left:30px;top:34px;width:315px;color:var(--text-dark)}
.packages .heading,.exclusive .heading{color:var(--violet);background:linear-gradient(90deg,var(--pink),#3b63d8);-webkit-background-clip:text;background-clip:text;-webkit-text-fill-color:transparent}
.packages .body,.exclusive .body{color:var(--text-dark);margin-top:10px}
.cap-dark{font-size:11px;font-weight:700;margin-top:12px;color:var(--text-dark)}
.packages .list,.exclusive .list{color:var(--text-dark);margin-top:6px}
.exclusive{left:30px;top:352px;width:315px;color:var(--text-dark)}
.two-col{display:grid;grid-template-columns:1fr 1fr;column-gap:10px}
.ph-pizza{left:0;top:640px;width:366px;height:138px;clip-path:polygon(0 26%,100% 0,100% 100%,0 100%);background:linear-gradient(120deg,#7a2e16,#c7702c 40%,#e7b45d 60%,#5a2a1a)}
</style>
</head>
<body>

<section class="spread spread--outside">
  <div class="panel p1 outside-p1">
    <div class="abs why">
      <h2 class="heading">Warum Zackfalke?</h2>
      <ul class="list">
        <li>Einzigartige Kombination aus Spiel, Erlebnis &amp; Teambuilding</li>
        <li>Fördert Teamgeist, Kommunikation &amp; Motivation</li>
        <li>Wetterunabhängig &amp; planungssicher</li>
        <li>Geeignet für kleine Teams &amp; große Gruppen</li>
        <li>Persönliche Betreuung &amp; flexible Eventplanung möglich</li>
      </ul>
      <strong>Teambuilding, das Spaß macht – und nachhaltig wirkt.</strong>
    </div>
    <div class="photo photo-toast" role="img" aria-label="Foto: Gruppe stößt mit Sektgläsern an, lachende Frau im Vordergrund"></div>
  </div>

  <div class="photo photo-crowd" role="img" aria-label="Foto: jubelnde Gruppe junger Leute in blauen Shirts"></div>

  <svg class="abs band" viewBox="0 0 733 778" aria-hidden="true">
    <defs>
      <linearGradient id="fadeTop" x1="0" y1="0" x2="0" y2="1">
        <stop offset="0" stop-color="#0a1024"/><stop offset=".22" stop-color="#0a1024" stop-opacity=".9"/><stop offset=".42" stop-color="#0a1024" stop-opacity="0"/>
      </linearGradient>
      <linearGradient id="stripe" x1="0" y1="0" x2="1" y2="0">
        <stop offset="0" stop-color="#19b9ec"/><stop offset="1" stop-color="#7a4bd8"/>
      </linearGradient>
    </defs>
    <rect width="733" height="300" fill="url(#fadeTop)"/>
    <polygon points="0,478 733,628 733,778 0,778" fill="#0a1330"/>
    <polygon points="0,468 733,618 733,628 0,478" fill="url(#stripe)"/>
  </svg>

  <div class="abs book">
    <h2 class="heading">Bucht jetzt eurer Team-Event oder lasst es uns gemeinsam plane</h2>
    <p class="body">Je nach gewünschtem Umfang könnt ihr eure Team-Event direkt online buchen oder mit uns gemeinsam planen. Eine direkte Buchung ist online auf unserer Website möglich.</p>
  </div>

  <div class="abs contact">
    <p>Für eine individuelle Planung<br>schickt uns gerne eine Mail.</p>
    <div class="entry"><div class="label">E-Mail:</div><div class="value">teamevent@zackfalke.de</div>
      <div class="label" style="margin-top:4px">Website:</div><div class="value">zackfalke.de</div></div>
    <p class="loc">Standort:</p>
    <p class="addr">A2-Autobahnabfahrt Nordkreuz auf dem<br>Autohof Musterhausen<br>Zackfalke Spaß-Erlebnis-Welt GmbH<br>Lindenfeldweg 7<br>38100 Musterhausen</p>
  </div>

  <h1 class="abs title">Teambuilding &amp; Firmenevents die nachhaltig verbinden</h1>
  <div class="abs title-rule"></div>
  <p class="abs sub">FÜR KLEINE UND GROSE TEAMS</p>

  <div class="abs brand"><span class="dot"></span>Zackfalke</div>

  <div class="abs ideal">
    <p class="cap">IDEAL FÜR:</p>
    <ul><li>Firmenfeiern</li><li>Sommerfeste</li><li>Weihnachtsfeiern</li><li>Team- &amp; Incentive-Events</li></ul>
  </div>

  <div class="abs bar">
    <span style="left:30px">Zackfalke – Wir bringen Teams in Bewegung.</span>
    <span style="left:403px">kostenlose Parkplätze</span>
    <span style="left:532px">optimal zu erreichen</span>
  </div>
</section>

<section class="spread spread--inside">
  <div class="abs team">
    <h2 class="heading">Gemeinsame Erlebnisse.<br>Starker Teamgeist.</h2>
    <div class="body">
      <p>Der moderne Arbeitsalltag stellt Teams täglich vor neue Herausforderungen. Umso wichtiger sind gemeinsame Erlebnisse, die Motivation fördern, Kommunikation stärken und den Teamzusammenhalt nachhaltig verbessern.</p>
      <p>Zackfalke bietet dafür den perfekten Rahmen: unsere innovative Spaß-Erlebnis-Welt, in der Teambuilding spielerisch, aktiv und mit jeder Menge Freude erlebt wird.</p>
      <p>Ob Teamevent, Firmenfeier oder Workshop-Abschluss – bei Zackfalke entsteht aus gemeinsamen Momenten ein echtes Wir-Gefühl.</p>
    </div>
  </div>

  <h2 class="abs heading world">Eine Erlebnis-Welt – viele Möglichkeiten.</h2>

  <article class="card card-blacklight">
    <div class="card-head"><span class="card-tag">SCHWARZLICHT</span><span class="card-title">3D-Schwarzlicht-<br>Minigolf</span></div>
    <div class="body">
      <p>Taucht ein in faszinierende 3D-Welten mit leuchtenden Farben, kreativen Bahnen und beeindruckenden Lichteffekten.</p>
      <p style="margin-top:4px">Unser Schwarzlicht-Minigolf verbindet Spaß mit lockerem Wettbewerb und eignet sich hervorragend für Teams mit unterschiedlichen Altersgruppen und Fitnesslevels.</p>
      <p class="sub-cap">Mehrwert für euer Team:</p>
    </div>
    <ul class="list"><li>Fördert Kommunikation &amp; Austausch</li><li>Sorgt für Auflockerung &amp; gemeinsame Erfolgsmomente</li><li>Ideal zum Kennenlernen und Teambuilding</li></ul>
    <div class="photo ph-golf" role="img" aria-label="Foto: Gruppe spielt Minigolf in leuchtender Schwarzlicht-Kulisse"></div>
  </article>

  <article class="card card-team">
    <div class="card-head"><span class="card-tag">TEAMKAMPF</span><span class="card-title">Teamkampf - Spiele im Stil<br>von „Duell der Stars“</span></div>
    <div class="body">
      <p>In abwechslungsreichen Mini-Challenges treten Teams gegeneinander an. Hier sind Wissen, Geschick, Schnelligkeit und Strategie gefragt. Die Spiele sorgen für Spannung, Emotionen und jede Menge Gesprächsstoff.</p>
      <p class="sub-cap">Effekte:</p>
    </div>
    <ul class="list"><li>Stärkt Zusammenhalt</li><li>Fördert Teamarbeit &amp; Ehrgeiz</li><li>Garantiert Spaß &amp; Dynamik</li></ul>
    <div class="photo ph-team" role="img" aria-label="Foto: Team feuert Spieler bei einer Geschicklichkeits-Challenge an"></div>
  </article>

  <article class="card card-pixel">
    <div class="card-head"><span class="card-tag">PIXEL</span><span class="card-title">Pixel Games</span></div>
    <div class="body">
      <p>Auf unserem digitalen Gamefloor trifft auf Bewegung und Reaktionsschnelligkeit. Ein rasantes Jump´n´run, das besonders für kleine Teams und zur Ergänzung geeignet ist.</p>
      <p style="margin-top:4px">Die Pixel Games verlangen Abstimmung im Team, schnelle Entscheidungen und kreative Lösungsansätze – modern, interaktiv und einzigartig.</p>
    </div>
    <div class="photo ph-pixel" role="img" aria-label="Foto: Spieler springen auf grün leuchtendem Pixel-Spielboden"></div>
  </article>

  <div class="panel p3 inside-p3">
    <div class="abs packages">
      <h2 class="heading">Unsere Teambuilding-Pakete</h2>
      <p class="body">Unsere Teambuilding-Pakete gibt es in der Komfort- und Premium-Variante. Je nach gewünschtem Umfang beinhalten diese Getränke, Snacks und Goodies und sind auf Wunsch individuell anpassbar. Gemeinsam mit euch gestalten wir ein Event, das perfekt zu euren Zielen, eurer Gruppengröße und eurem Zeitrahmen passt.</p>
      <p class="cap-dark">Erweiterungsmöglichkeiten:</p>
      <ul class="list"><li>Kombination aus mehreren Actions</li><li>Flexible Dauer (z. B. 2–5 Stunden)</li><li>Optional buchbare zusätzliche Getränke-Pakete</li><li>Bei Exklusivbuchung unserer Erlebniswelt auch externes Catering möglich</li></ul>
      <p class="body" style="margin-top:4px">Auf Wunsch erstellen wir ein maßgeschneidertes Angebot für euer Unternehmen.</p>
    </div>
    <div class="abs exclusive">
      <h2 class="heading">Exklusivbuchung &amp; individuelle Eventgestaltung</h2>
      <p class="body">Für besondere Anlässe und große Gruppen kann Zackfalke exklusiv gebucht werden – eure eigene Eventlocation, ganz ohne andere Gäste.</p>
      <p class="cap-dark">Ideal für:</p>
      <ul class="list two-col"><li>Firmenfeiern</li><li>Weihnachtsfeiern</li><li>Sommerfeste</li><li>Team- &amp; Incentive-Events</li></ul>
      <p class="cap-dark" style="margin-top:6px">Externes Catering möglich</p>
      <p class="body" style="margin-top:3px">Ihr habt besondere kulinarische Vorstellungen oder arbeitet mit einem festen Caterer zusammen? Nach Absprache ermöglichen wir externes Catering und individuelle Lösungen.</p>
    </div>
    <div class="photo ph-pizza" role="img" aria-label="Foto: Hände greifen nach Pizzastücken"></div>
  </div>
</section>

</body>
</html>
```